Business Card Design

Personal training studio. My colors are burnt orange and grey. Specializing in group training and total body composition change. Nutritional consultant and contest prep.

Target Market(s)

My audience are people who are looking for total body composition change as well as knowledge on how to effectively receive results in the gym that they are a member of.

Industry/Entity Type

Training

Contact Information for Business Card

Dr. Maris Thackery
Marisjthackery@plumvane.com
3129071436
2815 west Brell ave.
Fennmoor Illinois 60948

Colors
f37122
aaaaaa

Requirements
Must have
• Animphasis on gaining knowledge that will sustain them for a life time. Healthy results and notice me results.
Nice to have
• Card should correlate with the colors of the studio. Orange and grey. With black flooring with orange speckles in it.

```html
<!DOCTYPE html>
<html lang="en">
<head>
<meta charset="utf-8">
<title>Forge Room Fitness – Business Card</title>
<link rel="stylesheet" href="https://fonts.googleapis.com/css2?family=Open+Sans:wght@400;600;700&display=swap">
<style>
  :root {
    --backdrop: #2b2b2d;
    --card: #0d0d0d;
    --orange: #f37122;
    --grey: #aaaaaa;
    --light: #e6e6e6;
    --white: #ffffff;
  }
  * { box-sizing: border-box; margin: 0; padding: 0; }
  html, body {
    width: 1200px; height: 780px; overflow: hidden;
    background: var(--backdrop);
    font-family: "Open Sans", sans-serif;
  }
  .canvas {
    position: relative; width: 1200px; height: 780px;
    display: flex; align-items: center; justify-content: center; gap: 60px;
  }
  .card {
    position: relative; width: 510px; height: 292px;
    background: var(--card);
    box-shadow: 0 10px 30px rgba(0,0,0,.45);
    overflow: hidden;
  }
  .card-front { display: flex; align-items: center; justify-content: center; }
  .brand { display: flex; align-items: center; gap: 16px; }
  .brand-dot { flex: none; width: 54px; height: 54px; border-radius: 50%; background: var(--orange); }
  .brand-name {
    color: var(--white); font-weight: 700; font-size: 30px;
    letter-spacing: 1px; text-transform: uppercase; line-height: 1.1;
  }
  .card-back .brand { position: absolute; left: 34px; top: 38px; gap: 10px; }
  .card-back .brand-dot { width: 30px; height: 30px; }
  .card-back .brand-name { font-size: 17px; }
  .contact { position: absolute; left: 200px; top: 128px; width: 280px; }
  .contact-name { color: var(--light); font-size: 22px; font-weight: 400; padding-bottom: 8px; }
  .contact-rule { height: 2px; background: var(--orange); width: 240px; margin-bottom: 12px; }
  .contact-list { list-style: none; color: var(--orange); font-size: 13px; line-height: 1.45; }
  .contact-list li { display: flex; align-items: flex-start; gap: 8px; }
  .contact-list svg { flex: none; margin-top: 3px; }
  .contact-phone { font-weight: 700; font-size: 16px; }
  .contact-list .indent { padding-left: 20px; }
  .edge-band { position: absolute; left: 0; right: 0; bottom: 0; height: 6px; display: flex; }
  .edge-band .grey { flex: 0 0 45%; background: var(--grey); }
  .edge-band .orange { flex: 1; background: var(--orange); }
</style>
</head>
<body>
<main class="canvas">
  <section class="card card-front" aria-label="Card front">
    <div class="brand">
      <span class="brand-dot"></span>
      <span class="brand-name">Forge Room<br>Fitness</span>
    </div>
  </section>

  <section class="card card-back" aria-label="Card back">
    <div class="brand">
      <span class="brand-dot"></span>
      <span class="brand-name">Forge Room Fitness</span>
    </div>
    <div class="contact">
      <p class="contact-name">Dr. Maris Thackery</p>
      <div class="contact-rule"></div>
      <ul class="contact-list">
        <li class="contact-phone">
          <svg width="12" height="12" viewBox="0 0 24 24" aria-hidden="true"><circle cx="12" cy="12" r="11" fill="none" stroke="currentColor" stroke-width="2"/><path d="M8 6l3 3-2 2a8 8 0 004 4l2-2 3 3-2 2C10 18 6 14 6 8z" fill="currentColor"/></svg>
          <span>312 907 1436</span>
        </li>
        <li>
          <svg width="12" height="12" viewBox="0 0 24 24" aria-hidden="true"><path d="M12 2a7 7 0 017 7c0 5-7 13-7 13S5 14 5 9a7 7 0 017-7z" fill="currentColor"/><circle cx="12" cy="9" r="2.5" fill="#0d0d0d"/></svg>
          <span>2815 west Brell ave.</span>
        </li>
        <li class="indent">Fennmoor Illinois 60948</li>
        <li>
          <svg width="12" height="12" viewBox="0 0 24 24" aria-hidden="true"><circle cx="12" cy="12" r="10" fill="currentColor"/><path d="M2 12h20M12 2c4 4 4 16 0 20M12 2c-4 4-4 16 0 20" stroke="#0d0d0d" stroke-width="1.5" fill="none"/></svg>
          <span>Marisjthackery@plumvane.com</span>
        </li>
      </ul>
    </div>
    <div class="edge-band"><span class="grey"></span><span class="orange"></span></div>
  </section>
</main>
</body>
</html>
```